Marlowvane Services Website Design

We have most content but require a professional design. We have a logo already and will need it utilized along with several of the photos from the attached documentation.
First page should have our mission and Vision and the synapsis provided in the word document. Visitors will be prompted to select from one of our 3 divisions from this page.
Each division will have the same list of tabs : About, Services, Safety, Careers and Contact.
Photos on each divisions page should be representative of the divisions offerings. The word doc attached contains the requested content and we are open to edits that would complement and fill the website.
I like the Tornwick site www.tornwick-example.com - they are our competition so cant be modeled directly after this.
Please include prompts to request quote at each service page. align the format of the geotechnical page to the other 2 divisions.
I used chat gpt for some of the content so will need it optimized for SCO.

```html
<!DOCTYPE html>
<html lang="en">
<head>
<meta charset="utf-8">
<title>Marlowvane Services</title>
<link rel="stylesheet" href="https://fonts.googleapis.com/css2?family=Bebas+Neue&family=Poppins:wght@400;500;600&display=swap">
<style>
  :root {
    --red-deep: #a9151c;
    --red-mid: #b3222a;
    --red-soft: #c04a52;
    --red-button: #ec1c24;
    --brand-red: #e31e24;
    --white: #ffffff;
    --card-title: #3a3a3a;
    --card-text: #6a6a6a;
    --footer-bg: #161616;
    --footer-text: #8a8a8a;
  }
  * { box-sizing: border-box; margin: 0; padding: 0; }
  html, body { width: 758px; height: 1200px; overflow: hidden; }
  body {
    position: relative;
    font-family: "Poppins", sans-serif;
    color: var(--white);
    background: var(--red-deep);
  }
  .page-backdrop {
    position: absolute; left: 0; top: 0; width: 758px; height: 1148px;
    background:
      linear-gradient(125deg, rgba(255,255,255,0) 40%, rgba(255,255,255,0.16) 70%, rgba(255,255,255,0.05) 100%),
      linear-gradient(180deg, var(--red-mid) 0%, var(--red-deep) 60%, #b02630 100%);
  }
  .corner-panel {
    position: absolute; left: 0; top: 0; width: 278px; height: 321px;
    background: var(--white);
  }
  .brand-name {
    position: absolute;
    font-family: "Poppins", sans-serif;
    font-weight: 600;
    color: var(--brand-red);
    font-size: 17px;
    letter-spacing: 1.6px;
    line-height: 1;
  }
  .header-brand { left: 63px; top: 16px; }
  .hero-photo {
    position: absolute; left: 63px; top: 63px; width: 305px; height: 363px;
    background: linear-gradient(180deg, #cfdce3 0%, #b9c4ca 45%, #8d8f8d 70%, #6f6d68 100%);
  }
  .hero-title {
    position: absolute; left: 386px; top: 128px;
    font-family: "Bebas Neue", sans-serif;
    font-size: 74px; line-height: 62px;
    color: #f7f3f3;
  }
  .section-heading {
    position: absolute; left: 0; width: 758px; text-align: center;
    font-family: "Bebas Neue", sans-serif;
    font-size: 26px; line-height: 1;
  }
  .mission-heading { top: 511px; }
  .mission-text {
    position: absolute; left: 90px; width: 578px; top: 552px;
    text-align: center; font-size: 9.6px; line-height: 15.8px;
  }
  .division-heading { top: 689px; }
  .division-intro {
    position: absolute; left: 120px; width: 518px; top: 730px;
    text-align: center; font-size: 13.4px; line-height: 21.5px;
  }
  .division-card {
    position: absolute; top: 797px; width: 189px; height: 260px;
    background: var(--white);
  }
  .card-aerial { left: 83px; }
  .card-drilling { left: 285px; }
  .card-renewable { left: 487px; }
  .card-photo {
    position: absolute; left: 12px; top: 14px; width: 164px; height: 98px;
  }
  .photo-aerial { background: linear-gradient(180deg, #4f6a3a 0%, #6f7f52 50%, #8b8175 100%); }
  .photo-drilling { background: linear-gradient(180deg, #3f78c8 0%, #8fb0d8 50%, #9a8e5a 80%, #8a7a4a 100%); }
  .photo-renewable { background: linear-gradient(160deg, #2f6ab8 0%, #3f7fd0 60%, #5a8fd6 100%); }
  .card-title {
    position: absolute; left: 12px; top: 129px;
    font-family: "Bebas Neue", sans-serif;
    font-size: 15px; line-height: 1; color: var(--card-title);
  }
  .card-text {
    position: absolute; left: 12px; width: 164px; top: 156px;
    font-size: 6.8px; line-height: 12.7px; color: var(--card-text);
  }
  .card-button {
    position: absolute; left: 12px; top: 214px; width: 164px; height: 38px;
    background: var(--red-button); color: var(--white);
    font-size: 8.6px; font-weight: 600;
    display: flex; align-items: center; justify-content: center;
  }
  .card-renewable .card-button { width: 160px; }
  .site-footer {
    position: absolute; left: 0; top: 1148px; width: 758px; height: 52px;
    background: var(--footer-bg);
  }
  .footer-brand { left: 56px; top: 18px; }
  .copyright {
    position: absolute; left: 0; width: 758px; top: 19px;
    text-align: center; font-size: 9.6px; color: var(--footer-text);
  }
  .social-links { position: absolute; left: 597px; top: 21px; display: flex; gap: 10px; }
  .social-dot { width: 7px; height: 7px; border-radius: 50%; background: var(--white); }
</style>
</head>
<body>
  <div class="page-backdrop" role="img" aria-label="Red-toned photo of a boom lift reaching up to a wind turbine"></div>
  <div class="corner-panel"></div>
  <div class="brand-name header-brand">MARLOWVANE</div>

  <div class="hero-photo" role="img" aria-label="Two white boom trucks parked on a gravel yard under power lines"></div>
  <h1 class="hero-title">SAFETY.<br>QUALITY.<br>SERVICE.</h1>

  <h2 class="section-heading mission-heading">MISSION &amp; VISION</h2>
  <p class="mission-text">At Marlowvane Services, we are dedicated to delivering unparalleled aerial access, geotechnical drilling, and service and maintenance solutions, consistently exceeding our clients' expectations. Our vision is to be the leading provider of aerial access, geotechnical drilling, and service solutions, setting the standard for excellence in safety, efficiency, and environmental stewardship.</p>

  <h2 class="section-heading division-heading">SELECT DIVISION</h2>
  <p class="division-intro">Choose from one of our three specialized divisions to explore our services tailored to your industry needs:</p>

  <div class="division-card card-aerial">
    <div class="card-photo photo-aerial" role="img" aria-label="Boom truck on a muddy forest site"></div>
    <h3 class="card-title">AERIAL ACCESS</h3>
    <p class="card-text">Providing comprehensive aerial access solutions for efficient project execution.</p>
    <div class="card-button">Elevate Your Projects</div>
  </div>

  <div class="division-card card-drilling">
    <div class="card-photo photo-drilling" role="img" aria-label="Drilling rig beside a water tower on a grass field"></div>
    <h3 class="card-title">GEOTECHNICAL DRILLING</h3>
    <p class="card-text">Delivering advanced geotechnical drilling services to support ground investigations and analysis.</p>
    <div class="card-button">Dig Deeper</div>
  </div>

  <div class="division-card card-renewable">
    <div class="card-photo photo-renewable" role="img" aria-label="Boom lift extended toward a wind turbine against blue sky"></div>
    <h3 class="card-title">RENEWABLE ENERGY SERVICES</h3>
    <p class="card-text">Offering specialized services to support the renewable energy sector's infrastructure development.</p>
    <div class="card-button">Power Your Future</div>
  </div>

  <footer class="site-footer">
    <div class="brand-name footer-brand">MARLOWVANE</div>
    <p class="copyright">© 2024 by Marlowvane Services Inc.</p>
    <div class="social-links" aria-label="Social links">
      <span class="social-dot"></span><span class="social-dot"></span><span class="social-dot"></span>
    </div>
  </footer>
</body>
</html>
```